Coastal waterside shopping complex needs a billboard sign

"Harbour Verge" is the name of a building which comprises 4 shops in a coastal waterside location. We need a 2440mm (Wide) x 1100mm (High) "Harbour Verge" billboard design that will fit with the coastal theme but is modern and contemporary, positioning the building as a high class mini shopping complex.

The photo below is for reference only. We only need a design for the "Harbour Verge" sign.

The end product will need to be an EPS scalable vector file.

```html
<!DOCTYPE html>
<html lang="en">
<head>
<meta charset="utf-8">
<title>Harbour Verge – Billboard</title>
<link rel="stylesheet" href="https://fonts.googleapis.com/css2?family=League+Spartan:wght@800&display=swap">
<style>
  :root {
    --sea-top: #c3e5f2;
    --sea-mid-1: #84cfe2;
    --sea-mid-2: #3fa6c0;
    --sea-mid-3: #1d7893;
    --sea-deep: #15627f;
    --pane-top: #d6eff5;
    --pane-mid-1: #9fe2ec;
    --pane-mid-2: #5fd6e2;
    --pane-mid-3: #3ccdd6;
    --pane-bottom: #20a0cf;
    --frame: #ffffff;
    --ink: #04546a;
    --highlight: #ffffff;
    --ball-tone: #f04a52;
  }
  html, body {
    margin: 0;
    padding: 0;
    overflow: hidden;
    background: var(--sea-deep);
  }
  .billboard {
    position: relative;
    width: 1200px;
    height: 544px;
    overflow: hidden;
  }
  .sea-backdrop {
    position: absolute;
    inset: 0;
    background: linear-gradient(180deg,
      var(--sea-top) 0%,
      var(--sea-mid-1) 25%,
      var(--sea-mid-2) 55%,
      var(--sea-mid-3) 75%,
      var(--sea-deep) 85%,
      var(--sea-deep) 100%);
  }
  .title-pane {
    position: absolute;
    left: 128px;
    top: 68px;
    width: 822px;
    height: 392px;
    border: 5px solid var(--frame);
    background: linear-gradient(180deg,
      var(--pane-top) 0%,
      var(--pane-top) 12%,
      var(--pane-mid-1) 35%,
      var(--pane-mid-2) 58%,
      var(--pane-mid-3) 78%,
      var(--pane-bottom) 90%,
      var(--pane-bottom) 100%);
  }
  .billboard-title {
    position: absolute;
    left: 184px;
    top: 124px;
    margin: 0;
    font-family: "League Spartan", sans-serif;
    font-weight: 800;
    font-size: 156px;
    line-height: 150px;
    letter-spacing: 0;
    color: var(--ink);
    text-transform: uppercase;
    text-shadow: 7px 6px 0 var(--highlight);
    white-space: nowrap;
  }
  .billboard-title span { display: block; }
  .beach-ball {
    position: absolute;
    left: 846px;
    top: 364px;
    width: 124px;
    height: 124px;
    border-radius: 50%;
    background: var(--ball-tone);
  }
</style>
</head>
<body>
<main class="billboard">
  <div class="sea-backdrop" role="img" aria-label="Layered ocean wave illustration in shades of blue"></div>
  <div class="title-pane" role="img" aria-label="Layered turquoise wave illustration inside a white frame"></div>
  <h1 class="billboard-title"><span>Harbour</span><span>Verge</span></h1>
  <div class="beach-ball" role="img" aria-label="Illustration of a red and white beach ball"></div>
</main>
</body>
</html>
```